"Drink Champagne and Dance on the Table" sort of business card needed!

We throw events, weddings, engagement parties, baby showers and the sort of end of year corporate events that people remember long after the glitter has settled - the sort of events that make you stand still and say wow when you walk in and then make you want to "Drink Champagne and Dance on the Tables"

We have a great logo with heaps of potential and need a business card that just screams creative professionals!

We are based in Auckland, NZ and are priced at the Premium end of the market were there are around 10 other main competitors. We need to stand out and make a strong statement about who we are!

Our Business Card will be one of the few items that we print out so are fully prepared to invest in a premium print job.

We really love our logo and think it has heaps of potential! Its ok if you would like to manipulate it (maybe put it on an angle, or use the circle element on its own?).

Black and Gold is very striking, but its very done in our market so we would like to avoid a solid black background please

We have done a bit of an inspiration document to give you an idea of the sort of look and feel we are hoping to achieve.

Target Market(s)

Woman aged 30 - 45 with an income bracket of $70k +

Industry/Entity Type

Event Planning

Contact Information for Business Card

Marnie
hello@fennwhistle.co.nz
www.fennwhistle.co.nz
02739418207

Number of Pages Required

5+ page

Requirements
Must have
• Vibrant colours and design (we love the vibrant pink and gold in the inspiration file)
• We would love to see some colour and creativity (although the black and gold is very striking). Because we are doing such minimal print work I am happy for the cards to be a little more expensive so if you want to use cut outs, rounded corners, gold foil, non standard size etc I am happy for that too. I really want the wow factor.
Nice to have
• We would like the design to be double sided.
Should not have
• The logo colour changed
• Use of Purple or Green or solid black background.
• Wedding Photos!

```html
<!DOCTYPE html>
<html lang="en">
<head>
<meta charset="utf-8">
<title>Fenn Whistle – Business Card</title>
<link rel="stylesheet" href="https://fonts.googleapis.com/css2?family=Raleway:wght@300;600&display=swap">
<style>
  :root {
    --backdrop: #2f3a45;
    --gold-light: #ecd49a;
    --gold-mid: #d4b06a;
    --gold-deep: #b48a45;
    --pink: #d81b6a;
    --pink-deep: #a3134f;
    --ink: #8e1148;
  }
  * { margin: 0; padding: 0; box-sizing: border-box; }
  html, body {
    width: 1200px;
    height: 848px;
    overflow: hidden;
    background: var(--backdrop);
  }
  .stage {
    position: relative;
    width: 1200px;
    height: 848px;
    display: flex;
    align-items: center;
    justify-content: center;
  }
  .card {
    position: relative;
    width: 900px;
    height: 514px;
    border-radius: 30px;
    overflow: hidden;
    border: 7px solid var(--pink);
    box-shadow: 0 0 0 2px var(--pink-deep), 0 18px 40px rgba(0,0,0,0.45);
    font-family: "Raleway", sans-serif;
    color: var(--ink);
  }
  .card__surface {
    position: absolute;
    inset: 0;
    background:
      linear-gradient(115deg, rgba(255,255,255,0.35) 0%, rgba(255,255,255,0) 35%, rgba(255,255,255,0.18) 55%, rgba(0,0,0,0.08) 100%),
      linear-gradient(180deg, var(--gold-light) 0%, var(--gold-mid) 60%, var(--gold-deep) 100%);
  }
  .card__seal {
    position: absolute;
    left: 63px;
    top: 120px;
    width: 260px;
    height: 260px;
    border: 6px solid var(--pink);
    border-radius: 50%;
    display: flex;
    align-items: center;
    justify-content: center;
    text-align: center;
    font-size: 36px;
    font-weight: 600;
    line-height: 1.15;
    letter-spacing: 1px;
    color: var(--pink);
  }
  .card__details {
    position: absolute;
    left: 440px;
    top: 63px;
    width: 420px;
  }
  .brand {
    display: flex;
    align-items: center;
    gap: 20px;
  }
  .brand__circle {
    width: 88px;
    height: 88px;
    border: 4px solid var(--pink);
    border-radius: 50%;
    flex: none;
  }
  .brand__name {
    font-size: 36px;
    font-weight: 600;
    line-height: 1;
    color: var(--pink);
    white-space: nowrap;
  }
  .brand__tagline {
    margin-top: 8px;
    font-size: 12px;
    font-weight: 600;
    letter-spacing: 4px;
    text-transform: uppercase;
    color: var(--ink);
  }
  .person {
    margin-top: 38px;
    font-size: 40px;
    font-weight: 300;
    letter-spacing: 1px;
  }
  .contacts {
    list-style: none;
    margin-top: 18px;
  }
  .contacts__item {
    display: flex;
    align-items: center;
    gap: 14px;
    font-size: 25px;
    font-weight: 300;
    line-height: 1.65;
    white-space: nowrap;
  }
  .contacts__icon {
    width: 20px;
    height: 20px;
    flex: none;
    color: var(--pink);
  }
</style>
</head>
<body>
<main class="stage">
  <article class="card">
    <div class="card__surface" role="img" aria-label="Gold foil finish over light wood veneer"></div>

    <div class="card__seal">Fenn<br>Whistle</div>

    <section class="card__details">
      <div class="brand">
        <span class="brand__circle"></span>
        <div>
          <div class="brand__name">Fenn Whistle</div>
          <div class="brand__tagline">Weddings &amp; Events</div>
        </div>
      </div>

      <p class="person">Marnie</p>

      <ul class="contacts">
        <li class="contacts__item">
          <svg class="contacts__icon" viewBox="0 0 20 20" aria-hidden="true">
            <rect x="1.5" y="4" width="17" height="12" fill="none" stroke="currentColor" stroke-width="1.8"/>
            <path d="M1.5 4 L10 11 L18.5 4" fill="none" stroke="currentColor" stroke-width="1.8"/>
          </svg>
          hello@fennwhistle.co.nz
        </li>
        <li class="contacts__item">
          <svg class="contacts__icon" viewBox="0 0 20 20" aria-hidden="true">
            <circle cx="10" cy="10" r="8.2" fill="none" stroke="currentColor" stroke-width="1.6"/>
            <ellipse cx="10" cy="10" rx="3.6" ry="8.2" fill="none" stroke="currentColor" stroke-width="1.4"/>
            <path d="M2 10 H18 M3.5 6 H16.5 M3.5 14 H16.5" stroke="currentColor" stroke-width="1.3"/>
          </svg>
          www.fennwhistle.co.nz
        </li>
        <li class="contacts__item">
          <svg class="contacts__icon" viewBox="0 0 20 20" aria-hidden="true">
            <path d="M2 7 Q10 1 18 7 L16 9.5 L13 8 L13 6.5 Q10 5.5 7 6.5 L7 8 L4 9.5 Z" fill="currentColor"/>
            <rect x="4" y="10.5" width="12" height="7" rx="1.5" fill="currentColor"/>
            <circle cx="10" cy="14" r="2" fill="var(--gold-mid)"/>
          </svg>
          02739418207
        </li>
      </ul>
    </section>
  </article>
</main>
</body>
</html>
```